Graphic Design/Logo Needed for Ear Drops Bottle

We have an Ear Drop Medication that we need to create a new label for. We will use a retro picture of a Doctor (Dr. Halvane) and the name of the product is Mighty Lobe. There is no official logo, so we will want to create a retro, basic logo for Mighty Lobe and use the retro picture. Front portion of the label is Size is 1.5" in height, and about 1.375" Width. this is a small tube similar in size to eye drops. We will be looking for just the logo portion and what you will see on the front of the bottle.

Target Market(s)

Medical Container

Industry/Entity Type

Medical

Font styles to use
Serif
Sans Serif

Colors
0054AA
0677BA
7BADD7
CADEEF
E8F1F8
FFF300
FFF600
FEFA6F
FFFEC7
FFFEE8

Requirements
Must have
• Picture of Dr. Halvane, "Mighty Lobe", Dr. Halvane's Ear Solution
Nice to have
• Retro Style or Modern with Retro Feel, Clean and engaging

```html
<!DOCTYPE html>
<html lang="en">
<head>
<meta charset="utf-8">
<title>Mighty Lobe – Dr. Halvane's Ear Solution Label</title>
<link rel="stylesheet" href="https://fonts.googleapis.com/css2?family=Open+Sans:wght@700;800&family=Roboto+Slab:wght@700&display=swap">
<style>
  :root {
    --page: #ffffff;
    --label-bg: #ffffff;
    --label-edge: #1a1a1a;
    --band: #0aafd4;
    --ink: #111111;
    --brand-red: #d22328;
    --portrait-dark: #3b3434;
    --portrait-mid: #1d93b5;
  }
  * { box-sizing: border-box; margin: 0; padding: 0; }
  html, body {
    width: 1200px;
    height: 1200px;
    overflow: hidden;
    background: var(--page);
  }
  .canvas {
    position: relative;
    width: 1200px;
    height: 1200px;
  }
  .label {
    position: absolute;
    left: 220px;
    top: 162px;
    width: 760px;
    height: 876px;
    background: var(--label-bg);
    border: 1.5px solid var(--label-edge);
  }
  .label__band {
    position: absolute;
    left: 183px;
    top: -6px;
    width: 382px;
    bottom: 0;
    background: var(--band);
  }
  .label__portrait {
    position: absolute;
    left: 254px;
    top: 44px;
    width: 270px;
    height: 362px;
    border-radius: 120px 120px 20px 20px;
    background: linear-gradient(180deg, var(--portrait-dark) 0%, var(--portrait-dark) 60%, var(--portrait-mid) 100%);
  }
  .label__brand {
    position: absolute;
    left: 110px;
    top: 420px;
    width: 548px;
    text-align: center;
    font-family: "Open Sans", sans-serif;
    font-weight: 800;
    color: var(--brand-red);
    font-size: 116px;
    line-height: 1.02;
    letter-spacing: -1px;
  }
  .label__maker {
    position: absolute;
    left: 0;
    right: 0;
    top: 694px;
    text-align: center;
    font-family: "Open Sans", sans-serif;
    font-weight: 700;
    font-size: 60px;
    line-height: 1;
    color: var(--ink);
    letter-spacing: -0.5px;
  }
  .label__product {
    position: absolute;
    left: 183px;
    width: 382px;
    top: 772px;
    text-align: center;
    font-family: "Open Sans", sans-serif;
    font-weight: 700;
    font-size: 39px;
    line-height: 1;
    color: var(--ink);
  }
  .label__volume {
    position: absolute;
    right: 42px;
    top: 800px;
    font-family: "Roboto Slab", serif;
    font-weight: 700;
    font-size: 40px;
    line-height: 1;
    color: var(--ink);
    transform: scaleX(0.8);
    transform-origin: right center;
  }
</style>
</head>
<body>
  <main class="canvas">
    <section class="label">
      <div class="label__band"></div>
      <div class="label__portrait" role="img" aria-label="Retro illustration of Dr. Halvane wearing a head mirror, shirt and tie"></div>
      <h1 class="label__brand">Mighty<br>Lobe</h1>
      <p class="label__maker">DR. HALVANE'S</p>
      <p class="label__product">EAR SOLUTION</p>
      <p class="label__volume">30ML</p>
    </section>
  </main>
</body>
</html>
```